Tri Fold Brochure for Brookline Financial Planning SA

We need a tri fold and PDF (emailable) brochure for financial planning business located in a rural location in South Australia. I have attached the information we would like included. I would like the brochure to have a blue theme, as this is our corporate colour. I'm looking for something corporate, but not boring. It needs to catch the eye and engage our prospective clients. We have had some structural changes in the business and would like to portray a new company image that means business but is fresh and vibrant, yet very professional. It is possible that we could use the successful bid as a basis for our new website and further stationery needs.

Target Market(s)

Potential financial planning clients. We have a broad market 18-35 wealth accumulators, 35-50 wealth builders, 50-60 Pre-retirement, 60-75 retirement, 75+ Aged Care.

Industry/Entity Type

Financial Planning

Font styles to use
Sans Serif
Other font styles liked:
• Arial, verdana

Colors
0255a3
3176b5
85acd3
cfdeed
eaf1f7
ffffff
33a6d7
0392cd
85cae6

Requirements
Must have
• The Valmonte logo (which is in the uploaded material and cannot be changed), this needs to be placed close to the words as shown in the uploaded material. Our business logo. All the written information that I have attached less any design attributes I have attached. Some relatable photgraphs or images.
Nice to have
• The words "Certainty, Direction, and Peace of Mind" maybe in the back ground somewhere, sort of like a water mark. Any blue scheme is fine, with black and white included, take note of the version of blue in our logo. The fonts I have chosen can be used singularly or in a mixed format.
Should not have
• Photographs or designs used by other financial planning firms. Red, this is too confrontational.

```html
<!DOCTYPE html>
<html lang="en">
<head>
<meta charset="utf-8">
<title>Brookline Financial Planning SA – Tri Fold Brochure</title>
<link rel="stylesheet" href="https://fonts.googleapis.com/css2?family=Lato:wght@400;700;900&display=swap">
<style>
  :root {
    --navy: #0255a3;
    --royal: #0d57a8;
    --sky: #1a93d1;
    --cyan: #0392cd;
    --pale: #cfdeed;
    --mist: #eaf1f7;
    --white: #ffffff;
    --ink: #2b2b2b;
    --headline: #0f4fa8;
    --brand: #474c86;
  }
  * { margin: 0; padding: 0; box-sizing: border-box; }
  html, body { width: 1200px; height: 934px; overflow: hidden; background: var(--white); }
  body { font-family: "Lato", Arial, sans-serif; }
  .brochure { position: relative; width: 1200px; height: 934px; overflow: hidden; }

  .panel-left {
    position: absolute; left: 0; top: 0; width: 398px; height: 934px;
    background: linear-gradient(90deg, #e9e9e9 0%, #ffffff 12%, #ffffff 88%, #ececec 100%);
  }
  .panel-right {
    position: absolute; left: 792px; top: 0; width: 408px; height: 934px;
    background: linear-gradient(90deg, #f1f1f1 0%, #ffffff 10%);
  }
  .shapes { position: absolute; left: 0; top: 0; }

  .questions { position: absolute; left: 41px; top: 56px; width: 340px; color: var(--ink); }
  .questions p { font-size: 17px; line-height: 21.5px; margin-bottom: 14px; }

  .values { position: absolute; left: 40px; top: 546px; color: var(--cyan); }
  .values p { font-size: 44px; line-height: 66px; font-weight: 400; }
  .values .indent { padding-left: 12px; }

  .testimonial {
    position: absolute; left: 20px; top: 796px; width: 360px;
    text-align: center; font-size: 16.5px; line-height: 21.5px; color: var(--ink);
  }

  .contact {
    position: absolute; left: 398px; top: 498px; width: 394px;
    text-align: center; color: var(--white); font-weight: 700;
  }
  .contact h2 { font-size: 20px; font-weight: 700; margin-bottom: 28px; }
  .contact p { font-size: 20px; line-height: 25px; }
  .contact .gap { margin-top: 25px; }

  .headline {
    position: absolute; left: 800px; top: 58px; width: 388px;
    text-align: center; color: var(--headline);
    font-size: 26.5px; line-height: 32px; font-weight: 900; letter-spacing: -0.3px;
  }

  .brand-box {
    position: absolute; left: 928px; top: 766px; width: 200px; height: 130px;
    background: var(--white);
  }
  .brand-name {
    position: absolute; left: 930px; top: 764px;
    color: var(--brand); font-size: 29px; line-height: 33px; font-weight: 400;
  }
</style>
</head>
<body>
<div class="brochure">
  <div class="panel-left"></div>
  <div class="panel-right"></div>

  <svg class="shapes" width="1200" height="934" viewBox="0 0 1200 934">
    <defs>
      <linearGradient id="meetingTones" x1="0" y1="0" x2="1" y2="1">
        <stop offset="0" stop-color="#c9ccd0"/>
        <stop offset="0.5" stop-color="#9aa8b8"/>
        <stop offset="1" stop-color="#6f7f93"/>
      </linearGradient>
      <linearGradient id="officeTones" x1="0" y1="0" x2="0" y2="1">
        <stop offset="0" stop-color="#d8e2ec"/>
        <stop offset="0.5" stop-color="#8793a6"/>
        <stop offset="1" stop-color="#2a2f3e"/>
      </linearGradient>
    </defs>

    <!-- right panel blue band -->
    <polygon points="792,430 1200,268 1200,664 792,772" fill="var(--royal)"/>
    <!-- centre panel blue fields -->
    <polygon points="398,484 792,384 792,776 398,880" fill="var(--royal)"/>
    <polygon points="398,880 792,776 792,934 398,934" fill="var(--sky)"/>

    <!-- photo area: advisers meeting with clients -->
    <polygon class="photo" role="img" aria-label="Photo of smiling couple reviewing documents with an adviser"
             points="398,0 792,0 792,384 398,484" fill="url(#meetingTones)"/>

    <!-- photo area: two professionals in an office -->
    <polygon class="photo" role="img" aria-label="Photo of two business professionals standing in a bright office"
             points="773,300 1152,204 1152,652 773,730" fill="url(#officeTones)"/>

    <!-- accent square -->
    <rect x="756" y="254" width="112" height="146" fill="#1f8fd6" opacity="0.85"/>
  </svg>

  <section class="questions">
    <p>Are you looking for saving and investment advice to accumulate wealth?</p>
    <p>Are you ready to retire, or concerned that you may not have enough in your retirement savings?</p>
    <p>Have you recently sold a business or farm property?</p>
    <p>Are you concerned about your capacity to protect your wealth?</p>
    <p>Are you confident that your Estate will be distributed to your beneficiaries in accordance with your wishes?</p>
    <p>Do you need help with your Civicare Age Pension claim?</p>
    <p>Are you or a family member needing Aged Care and are worried about the costs?</p>
  </section>

  <section class="values">
    <p class="indent">“Certainty”</p>
    <p>“Direction”</p>
    <p>“Peace of mind”</p>
  </section>

  <blockquote class="testimonial">
    “We love working with clients who are seeking quality financial advice, and are keen to partner with us to achieve their goals.”<br>
    Daniel Harwood
  </blockquote>

  <section class="contact">
    <h2>Contact Us:</h2>
    <p>Phone: 08 8500 4172</p>
    <p>Email: office@brooklinefpsa.com.au</p>
    <p>Web: brooklinefpsa.com.au</p>
    <p class="gap">Brookline Financial Planning SA</p>
    <p>Level 1 14 Wattle Street</p>
    <p>LINDALE&nbsp; SA&nbsp; 5350</p>
  </section>

  <h1 class="headline">We Partner With Our<br>Clients To Create A Roadmap<br>For Their Financial Future....</h1>

  <div class="brand-box"></div>
  <div class="brand-name">Brookline<br>Financial<br>Planning SA</div>
</div>
</body>
</html>
```